IV Nutritional Clinic Web Design

We are working with Velmo. They are an IV Nutritional Clinic and in need of a new website design.
Some sites to use for inspiration:
https://brantlowcare.example
https://www.zolvarihealth.example
https://www.quellspa.example
https://pimrolift.example
https://www.dorvak-well.example/pages/iv-therapy-west-hollywood
https://www.tqoncowell.example/cancer-care/iv-drips/
https://drelmavita.example
https://salbrikmed.example
Thank you for taking the time to consider designing a website for us. We are web developers based in Stockton, CA, USA. Most of our projects go through the same process. Understanding this process may help you win a project with us. We custom-code all of our websites in-house. We don’t have any requirements as to what tools you use for your design, but we prefer Figma files. For any design that we label as four-stars, we send it to the client for review. The client picks the final design they want us to use. Once we complete this process, we will continue to show additional clients all the four-star sites and purchase them later. Your designs will have multiple chances to sell. For better chances of success, we ask that you follow these guidelines.
IMAGES:
If you use any images or icons in the design, we ask that you have a link to the asset so we can purchase the image/icon. Most of the designs we submit do not have the customer’s images on them unless they have some great images. Be creative; show us the feeling you are trying to portray with your image choices. Use any royalty-free site you choose. We subscribe to Corvix and mainly use their images, but we can purchase images outside of Corvix.
PLEASE NOTE: we will not submit designs to clients with watermarks on the images.
FONTS:
We ask that you identify the fonts used in the design. This can be done in a message if you want. We typically use Lumen Typeset and Corvix Fonts.
CONTENT:
We're always open to different content and ideas. We often submit designs with stock images so the client can see our vision. We typically take pictures after the website launch to use their images with our vision. Lorem Ipsum is fine for paragraphs, but we ask that you write the headers in correct English. We want to be able to show the vision and identify the sections of the website.
INSPIRATION:
We typically add a couple of links in the brief of websites we like to help you get started in your design.
REVISIONS:
We do not often ask for revisions of the designs unless we see something in the design that may not appeal to the client. If there are slight changes that we want to make, we do that in the development process.
FEEDBACK:
We rarely give feedback on designs during the design process. We are working on many website projects and do not have the time to provide feedback. We usually respond if your request is well thought out and asks specific questions, but a note asking “feedback, please” usually goes unanswered.
Number of Pages Required
1 page
Look and feel
Each slider illustrates characteristics of the customer's brand and the style your logo design should communicate.

```html
<!DOCTYPE html>
<html lang="en">
<head>
<meta charset="utf-8">
<title>Velmo Hydration – IV Nutritional Clinic</title>
<link rel="stylesheet" href="https://fonts.googleapis.com/css2?family=Merienda:wght@700;800&family=Montserrat:wght@400;500;600;700;800&display=swap">
<style>
:root{
  --green:#77a043;
  --navy:#1c2a87;
  --ink:#1b1b1b;
  --muted:#555;
  --band:#574f4d;
  --footer:#1c1e4b;
  --field:#f2f2f2;
  --white:#fff;
}
*{box-sizing:border-box;margin:0;padding:0}
html,body{width:1200px;height:4343px;overflow:hidden}
body{font-family:"Montserrat",Arial,sans-serif;color:var(--ink);background:var(--white);position:relative}
.abs{position:absolute}
.script{font-family:"Merienda",Georgia,serif;font-weight:800;font-style:italic;letter-spacing:-0.5px}
.btn{position:absolute;background:var(--navy);color:var(--white);font-size:13px;font-weight:600;display:flex;align-items:center;justify-content:center}
.photo{position:absolute}

/* hero */
.hero{position:absolute;left:0;top:0;width:1200px;height:597px;background:linear-gradient(110deg,#9aa3ae 0%,#c9ccd2 35%,#b7b8bd 60%,#8e929a 100%)}
.hero-shade{position:absolute;inset:0;background:linear-gradient(180deg,rgba(30,30,50,.35),rgba(30,30,50,.15) 60%,rgba(40,60,120,.2))}
.nav-logo{left:68px;top:18px;font-size:38px;font-weight:800;color:var(--navy);letter-spacing:1px}
.nav{left:350px;top:36px;display:flex;gap:40px;font-size:15px;color:var(--white)}
.nav a{color:inherit;text-decoration:none}
.nav .active{font-weight:700}
.nav-line{left:944px;top:82px;width:196px;height:1px;background:rgba(255,255,255,.7)}
.hero-kicker{left:0;width:1200px;top:212px;text-align:center;color:var(--white);font-size:20px;font-weight:600}
.hero-title{left:0;width:1200px;top:248px;text-align:center;color:var(--white);font-size:46px}
.hero-text{left:275px;width:650px;top:330px;text-align:center;color:var(--white);font-size:14px;line-height:22px}
.arrow{position:absolute;width:32px;height:32px;border-radius:50%;background:var(--white);display:flex;align-items:center;justify-content:center}

/* about */
.kicker{font-size:20px;font-weight:700;color:var(--ink)}
.h-green{color:var(--green)}
.about-text{left:70px;top:958px;width:515px;font-size:14px;line-height:22px;color:var(--ink)}

/* stats */
.stats{left:0;top:1173px;width:1200px;height:146px;background:var(--band);color:var(--white)}
.stat{position:absolute;top:34px;text-align:center}
.stat b{display:block;font-size:24px;font-weight:700}
.stat span{display:block;font-size:28px;margin-top:2px}
.stat-div{position:absolute;top:34px;width:1px;height:80px;background:rgba(255,255,255,.6)}

/* services */
.card-title{font-size:22px;font-weight:700}
.card-text{font-size:12px;line-height:22px;color:var(--muted);width:327px}
.read{font-size:14px;font-weight:700;color:var(--green);text-align:right;width:327px}

/* cta */
.cta{left:0;top:2561px;width:1200px;height:250px;background:linear-gradient(100deg,#6a6f78,#8c9099 45%,#767a84)}

/* why */
.num{position:absolute;width:54px;height:54px;border-radius:50%;border:1.5px solid #c9c9d6;color:var(--navy);font-size:22px;font-weight:700;display:flex;align-items:center;justify-content:center}
.why-title{position:absolute;width:320px;text-align:center;font-size:22px;font-weight:600;line-height:28px}
.why-text{position:absolute;width:270px;text-align:center;font-size:15px;line-height:22px;color:var(--muted)}

/* appointment */
.appt{left:0;top:3357px;width:1200px;height:578px;background:linear-gradient(110deg,#6e8aa8,#8aa3bb 40%,#4f6a8e 80%,#3f5b82)}
.field{position:absolute;left:332px;width:522px;height:47px;background:var(--field);border-radius:6px;font-size:12px;color:var(--ink);padding:14px 26px}

/* newsletter + footer */
.news{left:0;top:3935px;width:1200px;height:109px;background:var(--footer)}
.footer{left:0;top:4044px;width:1200px;height:299px;background:var(--footer);color:var(--white)}
.f-head{font-size:14px;font-weight:700;letter-spacing:.3px}
.f-list{font-size:15px;line-height:24px;list-style:none;margin-top:10px}
</style>
</head>
<body>

<!-- Hero -->
<section class="hero">
  <div role="img" aria-label="Nurse adjusting an IV drip beside a smiling patient in a hospital bed" class="photo" style="inset:0;background:linear-gradient(110deg,#a8b0ba,#d4d6da 45%,#b8b9bf 70%,#9aa0a9)"></div>
  <div class="hero-shade"></div>
  <div class="abs nav-logo">VELMO</div>
  <nav class="abs nav">
    <a class="active">Home</a><a>About</a><a>Services</a><a>Blog</a><a>Contact us</a>
  </nav>
  <div class="btn" style="left:944px;top:26px;width:182px;height:38px;font-size:13px">Book an Appointment</div>
  <div class="abs nav-line"></div>
  <div class="abs hero-kicker">Welcome to Velmo Hydration.</div>
  <h1 class="abs hero-title script">Your Health is Our Priority</h1>
  <p class="abs hero-text">we provide high-quality, compassionate care for you and your family. Our team of dedicated professionals is committed to ensuring that every patient receives the best treatment and attention possible.</p>
  <div class="btn" style="left:536px;top:410px;width:131px;height:38px">Discover More</div>
  <div class="arrow" style="left:63px;top:311px"><svg width="12" height="12" viewBox="0 0 12 12"><path d="M8 1 3 6l5 5" fill="none" stroke="#222" stroke-width="2"/></svg></div>
  <div class="arrow" style="left:1105px;top:311px"><svg width="12" height="12" viewBox="0 0 12 12"><path d="m4 1 5 5-5 5" fill="none" stroke="#222" stroke-width="2"/></svg></div>
</section>

<!-- About -->
<section>
  <div class="abs kicker" style="left:70px;top:698px">About Us</div>
  <h2 class="abs script h-green" style="left:70px;top:736px;width:520px;font-size:44px;line-height:62px">Whatever Your Healthcare Needs We Are Here to Help</h2>
  <p class="abs about-text">One of the key classifications is between traditio nal small molecule drugs; usually derived from chemical synthesis. Lorem ipsum dolor adipiscing incididunt ut labore dolor adipisc. Enim ad minim veniam rcitation ullamco laboris commodo consequat</p>
  <div class="btn" style="left:70px;top:1068px;width:135px;height:40px">More About Us</div>
  <div role="img" aria-label="Gloved hands drawing a blood sample from an arm with a tourniquet" class="photo" style="left:605px;top:677px;width:524px;height:438px;border-radius:90px 0 90px 0;background:linear-gradient(135deg,#e7e7ea,#cfd3da 50%,#b5bfca);box-shadow:0 4px 10px rgba(0,0,0,.15)"></div>
</section>

<!-- Stats -->
<section class="abs stats">
  <div class="stat" style="left:55px;width:160px"><b>+12</b><span class="script">Doctor</span></div>
  <div class="stat-div" style="left:282px"></div>
  <div class="stat" style="left:330px;width:230px"><b>+2500</b><span class="script">Happy Clients</span></div>
  <div class="stat-div" style="left:605px"></div>
  <div class="stat" style="left:640px;width:230px"><b>800</b><span class="script">Medical Beds</span></div>
  <div class="stat-div" style="left:917px"></div>
  <div class="stat" style="left:960px;width:205px"><b>100%</b><span class="script">Satisfaction</span></div>
</section>

<!-- Services -->
<section>
  <div class="abs kicker" style="left:62px;top:1397px">Our Services</div>
  <h2 class="abs script h-green" style="left:62px;top:1432px;width:720px;font-size:44px;line-height:62px">Our Velmo Hydration specialties Technical service</h2>
  <div class="btn" style="left:1008px;top:1403px;width:129px;height:40px">View Services</div>

  <div role="img" aria-label="IV drip bag held near a patient in a red cardigan" class="photo" style="left:62px;top:1597px;width:327px;height:300px;background:linear-gradient(135deg,#e9e9ec,#c9c6c8 50%,#9b2a2e)"></div>
  <div role="img" aria-label="Hand drawing vaccine from a small vial with a syringe" class="photo" style="left:436px;top:1597px;width:327px;height:300px;background:linear-gradient(135deg,#f0f0f2,#dcdfe4 60%,#c6cbd2)"></div>
  <div role="img" aria-label="Therapist treating a patient's leg in a bright clinic room" class="photo" style="left:809px;top:1597px;width:327px;height:300px;background:linear-gradient(135deg,#eeeeee,#d8d9db 55%,#8aa7c0)"></div>

  <div class="abs card-title" style="left:62px;top:1912px">IV Drips</div>
  <div class="abs card-title" style="left:436px;top:1912px">Vitamin Injection</div>
  <div class="abs card-title" style="left:809px;top:1912px">Therapy</div>
  <p class="abs card-text" style="left:62px;top:1950px">All the Lorem Ipsum generators on the Internet tend to repeat duos on predefined.</p>
  <p class="abs card-text" style="left:436px;top:1950px">All the Lorem Ipsum generators on the Internet tend to repeat duos on predefined.</p>
  <p class="abs card-text" style="left:809px;top:1950px">All the Lorem Ipsum generators on the Internet tend to repeat duos on predefined.</p>
  <div class="abs read" style="left:62px;top:2004px">Read more.</div>
  <div class="abs read" style="left:436px;top:2004px">Read more.</div>
  <div class="abs read" style="left:809px;top:2004px">Read more.</div>

  <div role="img" aria-label="Gloved hands adjusting a laboratory microscope under blue light" class="photo" style="left:62px;top:2047px;width:327px;height:300px;background:linear-gradient(135deg,#1f3f8a,#3e6ed2 50%,#16275a)"></div>
  <div role="img" aria-label="Clinicians working at desks with computer monitors" class="photo" style="left:436px;top:2047px;width:327px;height:300px;background:linear-gradient(135deg,#eef1f4,#d4dbe4 50%,#7894c0)"></div>
  <div role="img" aria-label="Doctor in a mask comforting an older couple on a sofa" class="photo" style="left:809px;top:2047px;width:327px;height:300px;background:linear-gradient(135deg,#b9b6b2,#8c8682 50%,#5f5c5c)"></div>

  <div class="abs card-title" style="left:62px;top:2362px">Laboratory</div>
  <div class="abs card-title" style="left:440px;top:2374px">Specialty Service</div>
  <div class="abs card-title" style="left:809px;top:2374px">Primary Care</div>
  <p class="abs card-text" style="left:62px;top:2400px">All the Lorem Ipsum generators on the Internet tend to repeat duos on predefined.</p>
  <p class="abs card-text" style="left:436px;top:2423px">All the Lorem Ipsum generators on the Internet tend to repeat duos on predefined.</p>
  <p class="abs card-text" style="left:809px;top:2423px">All the Lorem Ipsum generators on the Internet tend to repeat duos on predefined.</p>
  <div class="abs read" style="left:62px;top:2454px">Read more.</div>
  <div class="abs read" style="left:436px;top:2477px">Read more.</div>
  <div class="abs read" style="left:809px;top:2477px">Read more.</div>
</section>

<!-- Booking call to action -->
<section class="abs cta">
  <div role="img" aria-label="Patient's arm with an IV line resting on a hospital bed, nurse nearby" class="photo" style="inset:0;background:linear-gradient(100deg,rgba(80,84,92,.6),rgba(150,154,162,.4) 50%,rgba(90,94,104,.6))"></div>
  <h2 class="abs script" style="left:0;top:26px;width:1200px;text-align:center;color:var(--white);font-size:46px">Get the Care You Need – Book Now</h2>
  <p class="abs" style="left:210px;top:118px;width:780px;text-align:center;color:var(--white);font-size:14px;line-height:22px">A brief statement outlining the purpose and mission of the clinic. This can include the commitment to patient care, community health, and any specific goals or values.</p>
  <div class="btn" style="left:509px;top:178px;width:182px;height:40px;background:var(--white);color:var(--ink)">Book an Appointment</div>
</section>

<!-- Why choose us -->
<section>
  <div class="abs kicker" style="left:0;top:2888px;width:1200px;text-align:center">Why Choose Us</div>
  <h2 class="abs script h-green" style="left:150px;top:2928px;width:900px;text-align:center;font-size:44px;line-height:62px">We Are Always Open For Your Health Services</h2>
  <div class="abs" style="left:396px;top:3085px;width:1px;height:200px;background:#999"></div>
  <div class="abs" style="left:802px;top:3085px;width:1px;height:200px;background:#999"></div>

  <div class="num" style="left:167px;top:3073px">01</div>
  <div class="why-title" style="left:34px;top:3142px">Compassionate &amp; Expert Care</div>
  <p class="why-text" style="left:59px;top:3206px">Our team of dedicated healthcare professionals combines years of experience with a genuine commitment to providing care</p>

  <div class="num" style="left:573px;top:3073px">02</div>
  <div class="why-title" style="left:440px;top:3142px">Patient-Centered Approach</div>
  <p class="why-text" style="left:465px;top:3206px">Our team of dedicated healthcare professionals combines years of experience with a genuine commitment to providing care</p>

  <div class="num" style="left:979px;top:3073px">03</div>
  <div class="why-title" style="left:846px;top:3142px">Personalized Treatment Plans</div>
  <p class="why-text" style="left:871px;top:3206px">Our team of dedicated healthcare professionals combines years of experience with a genuine commitment to providing care</p>
</section>

<!-- Appointment form -->
<section class="abs appt">
  <div role="img" aria-label="Gloved hand holding an IV bottle above a masked nurse" class="photo" style="inset:0;background:linear-gradient(110deg,rgba(150,130,120,.35),rgba(120,150,180,.25) 40%,rgba(40,80,130,.35))"></div>
  <h2 class="abs script" style="left:0;top:42px;width:1200px;text-align:center;color:var(--white);font-size:46px">Make An Appointment</h2>
</section>
<div class="field" style="top:3478px">Name :</div>
<div class="field" style="top:3540px">Last Name :</div>
<div class="field" style="top:3603px">Email :</div>
<div class="field" style="top:3667px">Phone Number :</div>
<div class="field" style="top:3727px;height:110px">How can I Help You ?</div>
<div class="btn" style="left:487px;top:3854px;width:226px;height:37px;font-size:15px">Submit</div>

<!-- Newsletter -->
<section class="abs news">
  <h2 class="abs script" style="left:69px;top:22px;color:var(--white);font-size:44px">Subscribe for newsletter</h2>
  <div class="abs" style="left:650px;top:33px;width:326px;height:41px;background:var(--white);font-size:14px;font-weight:500;padding:12px 22px">Email Address</div>
  <div class="btn" style="left:1008px;top:33px;width:129px;height:41px;font-size:15px;background:#1e2f96">Subscribe</div>
</section>

<!-- Footer -->
<footer class="abs footer">
  <div class="abs" style="left:71px;top:26px;font-size:56px;font-weight:800;letter-spacing:4px">VELMO</div>
  <div class="abs" style="left:71px;top:96px;font-size:20px;font-weight:500;letter-spacing:12px">HYDRATION</div>
  <p class="abs" style="left:68px;top:144px;width:228px;font-size:14px;line-height:18px">Subscribe to out newsletter today to receive latest news administrate cost effective for tactical data.</p>

  <div class="abs" style="left:396px;top:34px"><div class="f-head">QUICK LINKS</div><ul class="f-list"><li>Home</li><li>About Us</li><li>Services</li><li>Blogs</li><li>Contact Us</li></ul></div>
  <div class="abs" style="left:650px;top:28px"><div class="f-head">CONTACT US</div><ul class="f-list"><li>1800-555-0148</li><li>care@velmohydration.example</li><li>Help &amp; Contact</li><li>FAQS</li></ul></div>
  <div class="abs" style="left:987px;top:28px"><div class="f-head">SERVICES</div><ul class="f-list"><li>Primary Care</li><li>Specialty Service</li><li>Laboratory</li><li>Wellness Programs</li><li>Facilities</li><li>Equipment</li></ul></div>

  <div class="abs" style="left:71px;top:260px;width:1070px;height:1px;background:rgba(255,255,255,.5)"></div>
  <div class="abs" style="left:76px;top:270px;font-size:14px;display:flex;gap:30px"><span>© 2024 Velmo Hydration. All Rights Reserved.</span><span>Terms &amp; Conditions</span><span>Privacy Policy</span></div>
  <svg class="abs" style="left:1018px;top:272px" width="100" height="16" viewBox="0 0 100 16" aria-label="Social links">
    <circle cx="8" cy="8" r="7" fill="#fff"/><circle cx="36" cy="8" r="7" fill="#fff"/><circle cx="64" cy="8" r="7" fill="#fff"/><circle cx="92" cy="8" r="7" fill="#fff"/>
  </svg>
</footer>

</body>
</html>
```